6 Sizes Set - Static Banners

We have an html template for our newsletter which include graphic elements and we need images to populate these fixed Grey spaces.

Attachment 1: PLEASE READ FULL Graphic Brief is the complete brief describing all fine details.

Attachment 2: layout, shows the example of template

Attachment 3: We need the 6 image sizes (i.e. different fonts, backgrounds, colors, casino icons) – attached Styles Folder for an idea of the variety. These are just a few examples.

Target Market(s)

global

Industry/Entity Type

Casino

Requirements
Must have
• Refer to attach Full brief, for complete explanation
Nice to have
• Second Place: refer to Screenshot
Perfect example of what to submit

```html
<!DOCTYPE html>
<html lang="en">
<head>
<meta charset="utf-8">
<title>Casino Newsletter Banner Set</title>
<link rel="stylesheet" href="https://fonts.googleapis.com/css2?family=Lobster&family=Exo+2:wght@300;600&family=Francois+One&family=Merriweather:wght@700&family=Roboto+Condensed:wght@700&display=swap">
<style>
:root{
  --page-light:#ececec;
  --page-dark:#bdbdbd;
  --gold:#ffd02a;
  --gold-deep:#e79a00;
  --lime:#a8e000;
  --green-top:#2f9e1c;
  --green-bottom:#0b5205;
  --coal-top:#2b2b2b;
  --coal-bottom:#0c0c0c;
  --teal-top:#1c6a80;
  --teal-bottom:#05303c;
  --purple-top:#6c1fa0;
  --purple-bottom:#360757;
  --red-top:#b8122e;
  --red-bottom:#680516;
  --silver:#e9e9ef;
  --ice:#d8ecf2;
  --notch:#f2f2f2;
}
*{box-sizing:border-box;margin:0;padding:0}
html,body{width:1200px;height:900px;overflow:hidden}
body{background:radial-gradient(ellipse at 50% 45%,var(--page-light) 0%,#d6d6d6 60%,var(--page-dark) 100%);position:relative;font-family:"Roboto Condensed",sans-serif}

.banner{position:absolute;left:var(--x);top:var(--y);width:var(--w);height:var(--h);overflow:hidden;display:flex;align-items:center;justify-content:center;text-align:center}
.banner::after{content:"";position:absolute;left:50%;bottom:0;transform:translateX(-50%);border:6px solid transparent;border-bottom-color:var(--notch)}
.strip::after{bottom:auto;top:0;border-bottom-color:transparent;border-top-color:var(--notch)}
.icon::after,.mini::after{display:none}
.strip{--w:200px;--h:48px}
.tile{--w:200px;--h:130px}
.wide{--w:640px;--h:90px;--x:295px}
.icon{--w:70px;--h:80px;--x:983px;border-radius:14px}
.mini{--w:45px;--h:45px;--x:1093px}

.art{position:absolute;border-radius:6px;opacity:.9}
.title{position:relative;line-height:.95}

/* themes */
.blackjack{background:linear-gradient(var(--green-top),var(--green-bottom))}
.blackjack .title{font-family:"Lobster",cursive;color:var(--gold);text-shadow:0 2px 0 #6b4100}
.blackjack .art{background:linear-gradient(135deg,#fff,#e6dcc8)}
.cash{background:linear-gradient(var(--coal-top),var(--coal-bottom))}
.cash .title{font-family:"Exo 2",sans-serif;font-weight:300;color:#fff}
.cash .title b{font-weight:600;color:var(--lime)}
.cash .art{background:linear-gradient(135deg,#d9e8cf,#7c9a6c)}
.games{background:radial-gradient(ellipse at 35% 30%,var(--teal-top),var(--teal-bottom))}
.games .title{font-family:"Francois One",sans-serif;color:var(--ice);text-shadow:0 0 3px #000,0 2px 4px #000}
.games .art{background:radial-gradient(circle,#c9a36a,#7a1a12 60%,#3b2414)}
.jackpots{background:linear-gradient(var(--purple-top),var(--purple-bottom))}
.jackpots .title{font-family:"Merriweather",serif;color:var(--silver);text-shadow:0 2px 2px #1a0030}
.jackpots .art{background:linear-gradient(135deg,#f3c63a,#b57a12)}
.vip{background:radial-gradient(ellipse at 50% 40%,var(--red-top),var(--red-bottom))}
.vip .title{font-family:"Francois One",sans-serif;color:var(--gold);text-shadow:0 2px 0 #5a0000}
.vip .art{background:linear-gradient(135deg,#ffd45a,#e07b00)}

/* sizes */
.strip .title{font-size:19px}
.tile .title{font-size:30px}
.wide .title{font-size:40px}
.wide.games .title,.wide.vip .title{font-size:44px}
.icon .title{font-size:16px}
.icon .title small{display:block;font-size:10px;font-family:"Roboto Condensed",sans-serif;color:#fff;margin-top:2px}
.mini .title{font-size:11px}
.mini .title small{display:block;font-size:7px}

/* buttons */
.cta{position:absolute;left:var(--x);top:var(--y);width:157px;height:44px;border-radius:4px;display:flex;align-items:center;padding:0 8px 0 18px;color:#fff;font-size:17px;text-decoration:none;box-shadow:0 1px 2px rgba(0,0,0,.4);background:linear-gradient(var(--c1),var(--c2))}
.cta span{flex:1}
.cta svg{width:28px;height:28px}
.cta.small-text{font-size:15px;padding-left:8px}
.cta-blue{--c1:#3552d6;--c2:#101f7a}
.cta-green{--c1:#2a9a1c;--c2:#0b4a05}
.cta-teal{--c1:#1c5a6e;--c2:#051e28}
.cta-purple{--c1:#6a1a96;--c2:#2c0448}
.cta-sky{--c1:#27a2e6;--c2:#0a5aa0}
.cta-coal{--c1:#3a3a3a;--c2:#0f0f0f}
.cta-red{--c1:#a8102a;--c2:#55030f}
</style>
</head>
<body>
<svg width="0" height="0" style="position:absolute">
  <defs>
    <radialGradient id="play-fill" cx="40%" cy="35%" r="70%"><stop offset="0" stop-color="#ffe866"/><stop offset="1" stop-color="#f0a000"/></radialGradient>
    <symbol id="play" viewBox="0 0 28 28"><circle cx="14" cy="14" r="13" fill="url(#play-fill)" stroke="#222" stroke-width="1.5"/><path d="M11 8l9 6-9 6z" fill="#1a1a1a"/></symbol>
  </defs>
</svg>

<!-- top strip -->
<div class="banner strip blackjack" style="--x:56px;--y:22px"><div class="art" role="img" aria-label="Playing cards" style="right:4px;top:2px;width:48px;height:40px"></div><p class="title">Blackjack<br>Tournaments</p></div>
<div class="banner strip cash" style="--x:282px;--y:22px"><div class="art" role="img" aria-label="Cash bundles" style="right:4px;top:6px;width:40px;height:36px"></div><p class="title">» Free <b>Cash</b><br><b>Giveaway</b></p></div>
<div class="banner strip games" style="--x:502px;--y:22px"><div class="art" role="img" aria-label="Dice and roulette wheel" style="right:8px;top:8px;width:80px;height:40px"></div><p class="title" style="margin-right:80px">HOT FREE<br>GAMES</p></div>
<div class="banner strip jackpots" style="--x:722px;--y:22px"><div class="art" role="img" aria-label="Slot machine reels and coins" style="right:4px;top:4px;width:46px;height:40px"></div><p class="title">Jackpots<br>Mania</p></div>
<div class="banner strip vip" style="--x:946px;--y:22px"><div class="art" role="img" aria-label="Cocktail glass" style="left:8px;top:6px;width:14px;height:34px"></div><p class="title">VIP REWARDS</p></div>

<!-- tiles -->
<div class="banner tile blackjack" style="--x:54px;--y:102px"><div class="art" role="img" aria-label="Playing cards" style="right:6px;top:2px;width:80px;height:52px"></div><p class="title" style="margin-top:36px">Blackjack<br>Tournaments</p></div>
<div class="banner tile cash" style="--x:54px;--y:245px"><div class="art" role="img" aria-label="Flying cash bundles" style="left:6px;top:4px;width:188px;height:32px;opacity:.6"></div><p class="title" style="font-size:24px;margin-top:18px">» Free <b>Cash</b><br><b>Giveaway</b></p></div>
<div class="banner tile games" style="--x:54px;--y:389px"><div class="art" role="img" aria-label="Roulette wheel, dice and lottery balls" style="right:0;bottom:0;width:60px;height:46px"></div><p class="title">HOT FREE<br>GAMES</p></div>
<div class="banner tile jackpots" style="--x:54px;--y:535px"><div class="art" role="img" aria-label="Slot machine reels" style="right:0;bottom:14px;width:46px;height:48px"></div><p class="title" style="font-size:28px;margin-right:20px">Jackpots<br>Mania</p></div>
<div class="banner tile vip" style="--x:54px;--y:681px"><div class="art" role="img" aria-label="Cocktail glass" style="left:34px;top:8px;width:30px;height:42px"></div><p class="title" style="margin-top:30px">VIP<br>REWARDS</p></div>

<!-- wide banners -->
<div class="banner wide blackjack" style="--y:102px"><div class="art" role="img" aria-label="Playing cards" style="right:30px;top:4px;width:130px;height:84px"></div><p class="title" style="margin-right:120px">Blackjack Tournaments</p></div>
<div class="banner wide cash" style="--y:208px"><div class="art" role="img" aria-label="Cash bundles" style="left:0;top:0;width:110px;height:90px;opacity:.5"></div><div class="art" role="img" aria-label="Cash bundles" style="right:0;top:0;width:120px;height:90px;opacity:.5"></div><p class="title" style="font-size:36px">» Free <b>Cash Giveaway</b></p></div>
<div class="banner wide games" style="--y:316px"><div class="art" role="img" aria-label="Roulette wheel, dice and lottery balls" style="right:0;top:4px;width:230px;height:86px"></div><p class="title" style="margin-right:230px">HOT FREE GAMES</p></div>
<div class="banner wide jackpots" style="--y:429px"><div class="art" role="img" aria-label="Slot machine reels" style="left:30px;top:4px;width:80px;height:70px"></div><div class="art" role="img" aria-label="Scattered gold coins" style="right:20px;top:4px;width:110px;height:82px;opacity:.6"></div><p class="title">Jackpots Mania</p></div>
<div class="banner wide vip" style="--y:539px"><div class="art" role="img" aria-label="Cocktail glass" style="left:122px;top:14px;width:26px;height:58px"></div><p class="title" style="margin-left:30px">VIP REWARDS</p></div>

<!-- app icons -->
<div class="banner icon blackjack" style="--y:96px"><p class="title">Black<br>jack<small>TOURNAMENTS</small></p></div>
<div class="banner icon cash" style="--y:204px"><p class="title" style="font-size:15px">Free<br><b>Cash</b><small style="color:var(--lime)">Giveaway</small></p></div>
<div class="banner icon games" style="--y:312px"><p class="title" style="font-size:14px;margin-bottom:24px">HOT FREE<br>GAMES</p><div class="art" role="img" aria-label="Dice" style="left:22px;bottom:8px;width:30px;height:18px"></div></div>
<div class="banner icon jackpots" style="--y:425px"><p class="title" style="font-size:13px;margin-bottom:34px">Jackpots<small>MANIA</small></p><div class="art" role="img" aria-label="Slot machine reels" style="left:10px;bottom:4px;width:50px;height:30px"></div></div>
<div class="banner icon vip" style="--y:535px"><p class="title" style="font-size:24px;margin-bottom:20px">VIP<small>REWARDS</small></p><div class="art" role="img" aria-label="Stack of gold coins" style="left:24px;bottom:6px;width:22px;height:16px"></div></div>

<!-- mini icons -->
<div class="banner mini blackjack" style="--y:116px"><p class="title">Black<br>jack</p></div>
<div class="banner mini cash" style="--y:222px"><p class="title">Free<br><b>Cash</b></p></div>
<div class="banner mini games" style="--y:330px"><p class="title" style="font-size:9px">HOT FREE<br>GAMES</p></div>
<div class="banner mini jackpots" style="--y:443px"><p class="title" style="font-size:9px;font-family:'Francois One',sans-serif">JACKPOTS<br>MANIA</p></div>
<div class="banner mini vip" style="--y:549px"><p class="title" style="font-size:14px">VIP<small>REWARDS</small></p></div>

<!-- call-to-action buttons -->
<a class="cta cta-blue" style="--x:364px;--y:696px"><span>Click Here</span><svg><use href="#play"/></svg></a>
<a class="cta cta-green" style="--x:540px;--y:696px"><span>Play Now</span><svg><use href="#play"/></svg></a>
<a class="cta cta-teal" style="--x:717px;--y:696px"><span>Join Free</span><svg><use href="#play"/></svg></a>
<a class="cta cta-purple small-text" style="--x:895px;--y:696px"><span>Join Here Now</span><svg><use href="#play"/></svg></a>
<a class="cta cta-sky" style="--x:451px;--y:761px"><span>More info</span><svg><use href="#play"/></svg></a>
<a class="cta cta-coal" style="--x:627px;--y:761px"><span>Learn more</span><svg><use href="#play"/></svg></a>
<a class="cta cta-red small-text" style="--x:804px;--y:761px"><span>Register for Free</span><svg><use href="#play"/></svg></a>
</body>
</html>
```